Buisness cards for international property developer
Morelli Costruzioni Group
Professional
Beatrice Solange Morelli
CEO
Head Office: Via Campo Lungo 158 00149 Rome Italy
beatrice.morelli@morellicostruzionigroup.com
www.morellicostruzionigroup.com

```html
<!DOCTYPE html>
<html lang="en">
<head>
<meta charset="utf-8">
<title>Morelli Costruzioni Group – Business Cards</title>
<link href="https://fonts.googleapis.com/css2?family=Cinzel:wght@500&family=PT+Sans:wght@400;700&display=swap" rel="stylesheet">
<style>
  :root {
    --stage: #2b2b2c;
    --paper: #ffffff;
    --gold-dark: #a86f22;
    --gold-mid: #d29d45;
    --gold-light: #ecc67e;
    --ink-on-gold: #ffffff;
    --shadow: rgba(0,0,0,0.45);
  }
  * { margin: 0; padding: 0; box-sizing: border-box; }
  html, body { width: 1200px; height: 901px; overflow: hidden; background: var(--stage); }
  .stage { position: relative; width: 1200px; height: 901px; }
  .card {
    position: absolute; left: 280px; width: 640px; height: 366px;
    background: var(--paper); box-shadow: 0 14px 30px var(--shadow); overflow: hidden;
  }
  .card--front { top: 60px; display: flex; flex-direction: column; align-items: center; justify-content: center; }
  .card--back { top: 475px; display: flex; }

  .brand { display: flex; flex-direction: column; align-items: center; gap: 14px; }
  .brand__square { width: 86px; height: 86px; background: linear-gradient(135deg, var(--gold-dark), var(--gold-light) 50%, var(--gold-mid)); }
  .brand__name { font-family: "Cinzel", serif; font-weight: 500; font-size: 25px; color: var(--gold-dark); letter-spacing: 0.5px; }
  .brand__cities { font-family: "Cinzel", serif; font-weight: 500; font-size: 10px; letter-spacing: 4px; color: #555; margin-top: -8px; }

  .back__mark-side { width: 150px; display: flex; align-items: center; justify-content: center; }
  .back__square { width: 92px; height: 150px; background: linear-gradient(160deg, var(--gold-dark), var(--gold-light) 50%, var(--gold-mid)); }
  .back__panel {
    flex: 1; padding: 40px 34px;
    background: linear-gradient(115deg, var(--gold-dark) 0%, var(--gold-mid) 40%, var(--gold-light) 70%, var(--gold-mid) 100%);
    color: var(--ink-on-gold); font-family: "PT Sans", sans-serif;
  }
  .person__name { font-weight: 700; font-size: 22px; }
  .person__role { font-size: 13px; margin-bottom: 12px; }
  .office__label { font-weight: 700; font-size: 13px; }
  .contact { list-style: none; font-size: 13px; line-height: 1.65; }
  .contact li { display: flex; align-items: center; gap: 7px; }
  .contact svg { width: 12px; height: 12px; flex: none; }
  .back__brand { margin-top: 16px; }
  .back__brand-name { font-family: "Cinzel", serif; font-weight: 500; font-size: 19px; }
  .back__brand-cities { font-family: "Cinzel", serif; font-size: 8px; letter-spacing: 3.5px; margin-left: 62px; }
</style>
</head>
<body>
<main class="stage">
  <section class="card card--front">
    <div class="brand">
      <div class="brand__square"></div>
      <div class="brand__name">Morelli Costruzioni Group</div>
      <div class="brand__cities">ROME · LONDON · NYC</div>
    </div>
  </section>

  <section class="card card--back">
    <div class="back__mark-side"><div class="back__square"></div></div>
    <div class="back__panel">
      <div class="person__name">Beatrice Solange Morelli</div>
      <div class="person__role">CEO</div>
      <div class="office__label">Head Office:</div>
      <ul class="contact">
        <li>Via Campo Lungo 158 00149 Rome, Italy</li>
        <li><svg viewBox="0 0 12 12"><path d="M2.5 1h2l1 2.5-1.3 1a6 6 0 0 0 3.3 3.3l1-1.3 2.5 1v2c0 .6-.4 1-1 1A9.5 9.5 0 0 1 1.5 2c0-.6.4-1 1-1z" fill="currentColor"/></svg>+39 06 555 0182</li>
        <li><svg viewBox="0 0 12 12"><rect x="1" y="2.5" width="10" height="7" fill="none" stroke="currentColor"/><path d="M1 2.5l5 4 5-4" fill="none" stroke="currentColor"/></svg>beatrice.morelli@morellicostruzionigroup.com</li>
        <li><svg viewBox="0 0 12 12"><circle cx="6" cy="6" r="5" fill="none" stroke="currentColor"/><ellipse cx="6" cy="6" rx="2.2" ry="5" fill="none" stroke="currentColor"/><path d="M1 6h10" stroke="currentColor"/></svg>www.morellicostruzionigroup.com</li>
      </ul>
      <div class="back__brand">
        <div class="back__brand-name">Morelli Costruzioni Group</div>
        <div class="back__brand-cities">ROME · LONDON · NYC</div>
      </div>
    </div>
  </section>
</main>
</body>
</html>
```